FC Quintel and Canvas flyer for our communications

1. Introduction:
FC Quintel is a dynamic and passionate amateur football club, consisting of approximately 600 members. We are looking to create a versatile Canvas poster template that can be used for various purposes, including promoting matches, announcing special events such as gala dinners or football tournaments, as well as for promoting our recruitment activities to schools.

2. Objective:
The aim of this project is to create an attractive and professional poster template that reflects the spirit of FC Quintel, while being easily adaptable for different types of communications. We want the template to convey the excitement, energy, and sense of belonging to our club, highlighting our primary colors (red and blue) as well as our logo.

3. Key Elements of the Template:
The template should include the following elements clearly and organized:

FC Quintel Logo: Ensure the club logo is displayed or even better a strong visual identification of the key element of the logo are easily recognizable on the poster.

Club Colors: Use the main FC Quintel colors (red and blue) dominantly to create a strong visual identification with the club.

Editable Spaces: Provide dedicated and editable spaces to include event-specific information such as date, time, venue, sponsor logos, and any other relevant content.

4. Layout and Composition:
The layout should be clean, balanced, and appealing, with clear visual hierarchy for each element. Ensure the template is flexible enough to accommodate different types of content while maintaining a consistent look.

5. Variants Options:
We would like to have different template variants, with slightly different layouts for match posters, special event announcements, and recruitment advertising posters. However, the core visual and key elements will remain the same.

6. Tone and Style:
The tone of the poster should be energetic, enthusiastic, and professional. Avoid overly cluttered elements and focus on simplicity and readability.

7. Format and Deliverables:
The template should be created in digital format (Canvas), with dimensions suitable for printing (e.g., A3 size) while also being compatible with digital media. Provide the template in an editable format (e.g., PSD or AI) as well as in final print-ready formats (PDF, JPG, PNG).

Target Market(s)

Fooball players, members of the club, parents of the kids of the clubs, sponsors

Industry/Entity Type

Football (soccer)

Font styles to use
Sans Serif

Colors
0054AA
0677BA
7BADD7
CADEEF
E8F1F8
0094D4
00A9DD
6FCCEA
C7EBF8
E9F6FB
EB3D1F
EC4F4E
F09395
F8D3D4
FCEDEE

Requirements
Must have
• Colors of the club

```html
<!DOCTYPE html>
<html lang="fr">
<head>
<meta charset="utf-8">
<title>FC Quintel – Affiche de match</title>
<link rel="stylesheet" href="https://fonts.googleapis.com/css2?family=Anton&family=Montserrat:wght@500;600;700;800&display=swap">
<style>
  :root {
    --club-red: #a82a27;
    --club-red-dark: #7d1f1e;
    --club-blue: #3f80bd;
    --stadium-top: #5e504a;
    --stadium-mid: #8f837d;
    --ink-light: #eeeef2;
    --ink-silver: #d6d6dc;
    --white: #ffffff;
    --shadow-red: #8e2522;
    --kit-blue: #2c4f8c;
  }
  html, body { margin: 0; padding: 0; overflow: hidden; background: #ffffff; }
  .poster {
    position: relative; width: 849px; height: 1200px; overflow: hidden;
    background: var(--club-red);
    font-family: "Montserrat", sans-serif; color: var(--white);
  }
  .stadium-photo {
    position: absolute; left: 0; top: 0; width: 849px; height: 400px;
    background: linear-gradient(180deg, var(--stadium-top) 0%, #7a6d67 30%, var(--stadium-mid) 55%, #9c5a54 80%, var(--club-red) 100%);
  }
  .backdrop { position: absolute; left: 0; top: 0; }
  .players-photo {
    position: absolute; left: 440px; top: 335px; width: 409px; height: 440px;
    background: radial-gradient(ellipse at 55% 50%, var(--kit-blue) 0%, #2a4a82 40%, rgba(44,79,140,0.45) 68%, rgba(168,42,39,0) 100%);
  }
  .club-mark {
    position: absolute; left: 12px; top: 14px; display: flex; align-items: center; gap: 8px;
    font-weight: 800; font-size: 21px; color: var(--white); letter-spacing: 0.5px;
  }
  .club-mark .dot { width: 18px; height: 18px; border-radius: 50%; background: var(--white); }
  .venue {
    position: absolute; left: 75px; width: 774px; top: 40px; text-align: center;
    font-family: "Anton", sans-serif; font-size: 64px; line-height: 72px; letter-spacing: 3px;
    color: var(--ink-light); text-shadow: 2px 3px 4px rgba(0,0,0,0.35);
  }
  .tag {
    position: absolute; z-index: 2; background: var(--club-blue); color: var(--white);
    box-shadow: 5px 5px 0 var(--shadow-red); text-align: center; white-space: nowrap;
  }
  .match-date { left: 270px; top: 113px; width: 315px; height: 40px; font-weight: 600; font-size: 27px; line-height: 40px; }
  .competition { position: absolute; left: 270px; width: 315px; top: 155px; text-align: center; font-weight: 600; font-size: 17px; }
  .home-team { left: 292px; top: 185px; width: 270px; height: 66px; font-weight: 600; font-size: 46px; line-height: 66px; letter-spacing: 1px; }
  .away-team {
    left: 270px; top: 258px; width: 315px; height: 74px;
    font-family: "Anton", sans-serif; font-size: 60px; line-height: 74px; letter-spacing: 2px; color: var(--ink-light);
    text-shadow: 2px 3px 3px rgba(0,0,0,0.35);
  }
  .headline {
    position: absolute; z-index: 2; left: 75px; top: 455px; display: flex; align-items: flex-end;
    font-family: "Anton", sans-serif; font-size: 150px; line-height: 150px; color: var(--ink-light);
    text-shadow: 3px 4px 6px rgba(0,0,0,0.35);
  }
  .trophy {
    width: 72px; height: 170px; margin: 0 -2px 8px -4px;
    background: linear-gradient(180deg, #f4f4f4 0%, #d9d9d9 30%, #e0b84a 45%, #b8862a 100%); border-radius: 36px 36px 8px 8px;
  }
  .ball-sponsors { position: absolute; left: 77px; top: 790px; width: 300px; }
  .section-title { font-weight: 800; font-size: 19px; line-height: 23px; color: var(--ink-silver); letter-spacing: 0.5px; margin: 0; }
  .ball-sponsors p { margin: 8px 0 0; font-weight: 500; font-size: 13.4px; line-height: 19.5px; color: var(--ink-light); }
  .sponsors { position: absolute; left: 77px; top: 945px; }
  .sponsor-box { position: absolute; left: 77px; top: 972px; width: 264px; height: 171px; background: var(--white); border-radius: 8px; }
  .side-event { position: absolute; left: 518px; top: 796px; width: 320px; }
  .event-name { font-family: "Anton", sans-serif; font-weight: 400; font-size: 33px; line-height: 42px; color: var(--ink-light); margin: 0; letter-spacing: 0.5px; text-shadow: 2px 2px 3px rgba(0,0,0,0.3); white-space: nowrap; }
  .event-place { margin: 14px 0 0; font-weight: 500; font-size: 13px; }
  .event-dates { margin: 22px 0 0; font-weight: 700; font-size: 12.4px; line-height: 19.5px; }
  .event-pitch { margin: 16px 0 0; font-family: "Anton", sans-serif; font-size: 27.5px; line-height: 33px; color: var(--ink-light); letter-spacing: 0.5px; text-shadow: 2px 2px 3px rgba(0,0,0,0.3); }
</style>
</head>
<body>
<div class="poster">
  <div class="stadium-photo" role="img" aria-label="Photo d'un grand stade vu depuis la pelouse, tribunes pleines"></div>

  <svg class="backdrop" width="849" height="1200" viewBox="0 0 849 1200" aria-hidden="true">
    <polygon points="502,889 512,926 420,1106 420,1200 348,1200" fill="var(--club-red-dark)"/>
    <polygon points="0,644 502,889 348,1200 0,1200" fill="var(--club-blue)"/>
    <polygon points="420,1106 849,1106 849,1200 376,1200" fill="var(--club-blue)"/>
  </svg>

  <div class="players-photo" role="img" aria-label="Photo de quatre joueurs en maillot bleu debout, l'un tenant un ballon"></div>

  <div class="club-mark"><span class="dot"></span>FC QUINTEL</div>

  <div class="venue">STADE DES PEUPLIERS</div>
  <div class="tag match-date">Sam 23 oct. à 18h30</div>
  <div class="competition">Championnat 2ème ligue</div>
  <div class="tag home-team">QUINTEL</div>
  <div class="tag away-team">VALMORIN</div>

  <div class="headline">W<span class="trophy" role="img" aria-label="Trophée doré surmonté d'un ballon de football"></span>nner</div>

  <div class="ball-sponsors">
    <h2 class="section-title">BALLONS DE<br>MATCH OFFERTS PAR :</h2>
    <p>Dorsaz Paysages SA, Paysagiste, Saxonnet Martine Roduit, Présidente de la commune de Quintel Pascal Vouilloz, Frabicant de brisoloirs, Quintel</p>
  </div>

  <h2 class="section-title sponsors">SPONSORS</h2>
  <div class="sponsor-box"></div>

  <div class="side-event">
    <h2 class="event-name">"La Grande Brisolée"</h2>
    <p class="event-place">à la Halle Rouge de Quintel</p>
    <p class="event-dates">Samedi 16 octobre 2021 de 14h à 22h<br>Dimanche 17 octobre 2021 de 10h à 17h</p>
    <p class="event-pitch">Brisolées et raclettes<br>servies par le FC Quintel<br>500 personnes maximum,<br>sans pass Covid.</p>
  </div>
</div>
</body>
</html>
```